Namecard Designs+Logo for a High End Automobile Company

We need a new business card for our company called Velta Motorhof.

www.veltamotorhof.example.sg
Our new website will be up in 2.5 months time.

We sell used and brand new continental cars like Korvane, QTL, Dravell, Solbrini and etc. Currently we are operating from 2 offices in Singapore and United Kingdom.

We want a design which is serious. We are open to colours but try to keep it at a maximum of 3 colours.

We prefer something simple and minimal. We are open to 2 sides printing or even 2 sided namecards. Both UK and Singapore company offices address must be in; either side by side, front and back, or even 2 sided cards.

The logo can be a text logo, emblem, abstract, pictorial or combination.

We are printing with Pribo.com so please kindly follow the printing guideline.

http://uk.pribo.example/help/faq/templates-and-guidelines.html

Rich and Car Enthusiasts

Printing

Must have
• Our 2 offices; UK and Singapore.

Our slogan which is " The Automobile Specialist"
Should not have
• Not more than 3 colours

```html
<!DOCTYPE html>
<html lang="en">
<head>
<meta charset="utf-8">
<title>Velta Motorhof – Business Cards</title>
<link rel="stylesheet" href="https://fonts.googleapis.com/css2?family=Open+Sans:ital,wght@0,700;1,700&family=Tinos&display=swap">
<style>
  :root {
    --page: #ffffff;
    --card-base: #dcd7d1;
    --card-light: #e9e5df;
    --brand-brown: #7a4a26;
  }
  * { margin: 0; padding: 0; box-sizing: border-box; }
  html, body { width: 1200px; height: 900px; overflow: hidden; background: var(--page); }
  .canvas { position: relative; width: 1200px; height: 900px; }
  .card {
    position: absolute; width: 532px; height: 350px;
    background: var(--card-base); overflow: hidden;
  }
  .card--front { left: 344px; top: 60px; }
  .card--back { left: 348px; top: 482px; }
  .card__shapes { position: absolute; inset: 0; width: 100%; height: 100%; }
  .card__shapes .light { fill: var(--card-light); }

  .brand { position: absolute; right: 18px; top: 16px; width: 150px; text-align: center; color: var(--brand-brown); }
  .brand__ring { display: block; margin: 0 auto 10px; }
  .brand__ring circle { fill: none; stroke: var(--brand-brown); stroke-width: 10; }
  .brand__name { font-family: "Open Sans", sans-serif; font-weight: 700; font-size: 17px; white-space: nowrap; }

  .slogan {
    position: absolute; left: 92px; top: 280px;
    transform-origin: left bottom; transform: rotate(-43deg);
    font-family: "Open Sans", sans-serif; font-style: italic; font-weight: 700;
    font-size: 20px; color: var(--brand-brown); white-space: nowrap;
  }

  .person { position: absolute; left: 46px; top: 218px; font-family: "Tinos", serif; color: var(--brand-brown); text-align: right; }
  .person__name { font-size: 23px; line-height: 1.1; }
  .person__title { font-size: 12px; }

  .office {
    position: absolute; transform-origin: left top; transform: rotate(-43deg);
    font-family: "Tinos", serif; color: var(--brand-brown); font-size: 10.5px; line-height: 12.5px; white-space: nowrap;
  }
  .office__name { font-size: 13.5px; line-height: 15px; }
  .office--uk { left: 70px; top: 124px; }
  .office--sg { left: 222px; top: 300px; }
</style>
</head>
<body>
<main class="canvas">
  <section class="card card--front" aria-label="Card front">
    <svg class="card__shapes" viewBox="0 0 532 350" aria-hidden="true">
      <path class="light" d="M0 0 H296 L142 160 Q128 174 114 161 L0 52 Z"/>
      <path class="light" d="M156 350 L322 178 Q336 164 350 177 L532 330 V350 Z"/>
    </svg>
    <div class="brand">
      <svg class="brand__ring" width="94" height="94" viewBox="0 0 94 94" aria-hidden="true"><circle cx="47" cy="47" r="41"/></svg>
      <div class="brand__name">Velta Motorhof</div>
    </div>
    <p class="slogan">The Automobile Specialist</p>
  </section>

  <section class="card card--back" aria-label="Card back">
    <svg class="card__shapes" viewBox="0 0 532 350" aria-hidden="true">
      <path class="light" d="M0 0 H296 L142 160 Q128 174 114 161 L0 52 Z"/>
      <path class="light" d="M156 350 L322 178 Q336 164 350 177 L532 330 V350 Z"/>
    </svg>
    <div class="brand">
      <svg class="brand__ring" width="94" height="94" viewBox="0 0 94 94" aria-hidden="true"><circle cx="47" cy="47" r="41"/></svg>
      <div class="brand__name">Velta Motorhof</div>
    </div>
    <div class="person">
      <p class="person__name">Marcus Hale</p>
      <p class="person__title">Managing Director</p>
    </div>
    <div class="office office--uk">
      <p class="office__name">UK Office</p>
      <p>27 Kestrel Row Harlow Quay</p>
      <p>mobile : 0400 555 018</p>
      <p>email : sales@velta.example.sg</p>
    </div>
    <div class="office office--sg">
      <p class="office__name">Singapore Office</p>
      <p>27 Kestrel Row Harlow Quay</p>
      <p>mobile : 0400 555 018</p>
      <p>email : sales@velta.example.sg</p>
    </div>
  </section>
</main>
</body>
</html>
```